Harborpoint Meridian Insurance Services

we are a high end insurance agency we specialize on Auto | Home | Business | Life looking for something professional and luxuries at the same time. if you guys need anything else please let me know.

Auto | Home | Business | Life must be under logo on the back with black background.

i want the back part to be black with our gold logo on it.

Target Market(s)

Auto | Home | Business | Life

Industry/Entity Type

Insurance Broker

Contact Information for Business Card

My logo is gold so a black in the back would be nice.

Font styles to use
Serif

Colors
000000

Requirements
Must have
• Big logo on the back with black background.

```html
<!DOCTYPE html>
<html lang="en">
<head>
<meta charset="utf-8">
<title>Harborpoint Meridian Insurance Services – Business Card</title>
<link rel="stylesheet" href="https://fonts.googleapis.com/css2?family=Cinzel:wght@400;600&family=Arimo:wght@400&display=swap">
<style>
  :root {
    --backdrop: #2b2b2d;
    --card: #050505;
    --card-edge: #111;
    --gold: #f2bb1a;
    --grey: #9a9a9a;
    --grey-light: #c9c9c9;
    --white: #f4f4f4;
    --arc: rgba(255,255,255,0.06);
  }
  * { box-sizing: border-box; margin: 0; padding: 0; }
  html, body { width: 1200px; height: 900px; overflow: hidden; }
  body {
    background: var(--backdrop);
    font-family: "Arimo", Arial, sans-serif;
    position: relative;
  }
  .card {
    position: absolute;
    left: 300px;
    width: 600px;
    height: 343px;
    background: var(--card);
    border: 1px solid var(--card-edge);
    box-shadow: 0 14px 30px rgba(0,0,0,0.55);
    overflow: hidden;
  }
  .card--front { top: 72px; }
  .card--back { top: 486px; }

  /* front */
  .front-arc { position: absolute; inset: 0; }
  .accent-bar {
    position: absolute;
    width: 26px; height: 9px;
    background: linear-gradient(90deg, #8c8c8c, #e0e0e0);
  }
  .accent-bar--tr { top: 58px; right: 0; }
  .accent-bar--bl { bottom: 16px; left: 0; }
  .front-brand {
    position: absolute;
    top: 112px; left: 0; right: 0;
    text-align: center;
  }
  .brand-mark {
    display: inline-block;
    width: 26px; height: 26px;
    border-radius: 50%;
    background: var(--gold);
    margin-bottom: 16px;
  }
  .brand-name {
    font-family: "Cinzel", Georgia, serif;
    font-weight: 600;
    color: var(--gold);
    line-height: 1.15;
  }
  .front-brand .brand-name { font-size: 30px; letter-spacing: 0.5px; }
  .front-brand .brand-name span { display: block; font-size: 17px; letter-spacing: 4px; }
  .services {
    position: absolute;
    top: 262px; left: 0; right: 0;
    text-align: center;
    color: var(--gold);
    font-size: 15px;
    letter-spacing: 1px;
    word-spacing: 3px;
  }
  .services .sep { color: var(--white); }

  /* back */
  .back-brand {
    position: absolute;
    top: 48px; left: 40px;
  }
  .back-brand .brand-name { font-size: 22px; }
  .back-brand .brand-name span { display: block; font-size: 12px; letter-spacing: 3px; }
  .side-bar {
    position: absolute;
    left: 0; top: 158px;
    width: 10px; height: 28px;
    background: var(--gold);
  }
  .person { position: absolute; top: 150px; left: 40px; }
  .person-name {
    font-family: "Cinzel", Georgia, serif;
    color: var(--white);
    font-size: 17px;
    letter-spacing: 1px;
  }
  .person-title { color: var(--gold); font-size: 14px; margin-top: 3px; }
  .address {
    position: absolute; top: 208px; left: 40px;
    color: var(--grey); font-size: 14px; line-height: 1.35;
  }
  .contact-list {
    position: absolute; top: 258px; left: 40px;
    list-style: none;
    color: var(--grey-light); font-size: 14px;
  }
  .contact-list li { display: flex; align-items: center; gap: 10px; height: 22px; }
  .contact-list svg { width: 12px; height: 12px; flex: none; }
</style>
</head>
<body>

<section class="card card--front" aria-label="Card front">
  <svg class="front-arc" viewBox="0 0 600 343" preserveAspectRatio="none" aria-hidden="true">
    <path d="M60 343 C 120 140, 480 140, 540 343 Z" fill="var(--arc)"/>
  </svg>
  <div class="accent-bar accent-bar--tr"></div>
  <div class="accent-bar accent-bar--bl"></div>
  <div class="front-brand">
    <div class="brand-mark"></div>
    <p class="brand-name">Harborpoint Meridian<span>Insurance Services</span></p>
  </div>
  <p class="services">AUTO <span class="sep">|</span> HOME <span class="sep">|</span> BUSINESS <span class="sep">|</span> LIFE</p>
</section>

<section class="card card--back" aria-label="Card back">
  <div class="back-brand">
    <p class="brand-name">Harborpoint Meridian<span>Insurance Services</span></p>
  </div>
  <div class="side-bar"></div>
  <div class="person">
    <p class="person-name">LORENA VASQUEL</p>
    <p class="person-title">Managing Director</p>
  </div>
  <p class="address">2750 Larkspur Ave<br>Bayfield, CA 92318</p>
  <ul class="contact-list">
    <li>
      <svg viewBox="0 0 12 12" aria-hidden="true"><path d="M2.5 1 L4.5 1 L5.2 3.6 L4 4.6 C4.6 6 5.8 7.3 7.4 8 L8.4 6.8 L11 7.5 L11 9.5 C11 10.3 10.3 11 9.5 11 C5 10.7 1.3 7 1 2.5 C1 1.7 1.7 1 2.5 1Z" fill="var(--gold)"/></svg>
      +1 555-014-2738
    </li>
    <li>
      <svg viewBox="0 0 12 12" aria-hidden="true"><rect x="1" y="2.5" width="10" height="7" fill="none" stroke="var(--gold)" stroke-width="1.3"/><path d="M1 2.5 L6 6.5 L11 2.5" fill="none" stroke="var(--gold)" stroke-width="1.3"/></svg>
      info@harborpointmeridian.com
    </li>
    <li>
      <svg viewBox="0 0 12 12" aria-hidden="true"><circle cx="6" cy="6" r="5" fill="none" stroke="var(--gold)" stroke-width="1.2"/><ellipse cx="6" cy="6" rx="2.2" ry="5" fill="none" stroke="var(--gold)" stroke-width="1"/><path d="M1 6 H11" stroke="var(--gold)" stroke-width="1"/></svg>
      www.harborpointmeridian.com
    </li>
  </ul>
</section>

</body>
</html>
```